Webbanner-Design für Versicherungsmakler
Zielgruppe
Wir führen eine ganzheitliche Betrachtung der individuellen finanziellen Situation des Kunden durch und erstellen auf dieser Basis ein persönliches Finanzkonzept. Wir haben uns spezialisiert auf die Beratung von Berufsunfähigkeitsversicherungen und der Altersvorsorge.
Aufgabenstellung
Es sollen Banner für Facebook-Seiten und Facebook-Werbeanzeigen erstellt werden. Sie stellen modern und ansprechend gestaltet sein. Es soll eine Interaktion beim Kunden angeregt werden. Das heißt, die Banner sollten entsprechend interessent gestaltet sein und neugierig machen.
Banner 1: Erstellung eines Versicherungsvergleichs
- Kunde soll aufgerufen werden sich einen Versicherungsvergleich erstellen zu lassen.
- Das Logo und der Weblink www.veltrama.de muss verwendet werden.
- Logo-Farben nutzen.
- Das Profilbild kann verwendet werden.
- Es soll auf eine Ersparnis mit bis zu 200 Euro im Jahr aufmerksam gemacht werden.
- Vorteil für den Kunden: richtige Versicherung finden, nur soviel bezahlen wie nötig.
Banner 2: Erstellung eines persönlichen Finanzkonzeptes
- Kunde soll aufgerufen werden sich ein Finanzkonzept erstellen zu lassen.
- Finanzkonzept beinhaltet alle Versicherungssparten, zeigt Versorungslücken bzw. eine Überversorgung auf. Gemeinsam ordnen wir dann mit dem Kunden seine Finanzsituation.
- Vorteil für den Kunden: Ganzheitliche Betrachtung der Finanzsituation, Nie mehr Kündigungstermine verpassen, richtige Versicherung finden, nur soviel bezahlen wie nötig.
18 - 99 Jahre
Alle Gehalts- und Bevölkerungsschichten
Grafiken/Gestaltung
Sie können unser Logo und das Profil-Bild benutzen, wenn sie zu eurem Design passt, ansonsten fügen bitte auf jedenfall eigene Grafiken (Lizenz muss vorhanden sein) ein.
Bitte Logo-Farben nutzen!
Format
- 1200x627px
- 470x264px

```html
<!DOCTYPE html>
<html lang="de">
<head>
<meta charset="utf-8">
<title>veltrama – Webbanner</title>
<link href="https://fonts.googleapis.com/css2?family=Montserrat:wght@400;500;600;700&family=Noto+Serif:wght@400&display=swap" rel="stylesheet">
<style>
  :root {
    --brand-red: #d0222b;
    --brand-red-dark: #b3161f;
    --ink: #3a3a3a;
    --ink-soft: #555;
    --paper: #ffffff;
    --mist: #ececec;
    --sea: #3cb8c6;
    --sea-light: #8fdde3;
    --snow: #e6eef6;
    --sky: #5a8fc8;
  }
  * { margin: 0; padding: 0; box-sizing: border-box; }
  html, body { width: 881px; height: 1200px; overflow: hidden; background: var(--paper); }
  .board { position: relative; width: 881px; height: 1200px; font-family: "Montserrat", sans-serif; }

  .banner {
    position: absolute; left: 262px; width: 359px; height: 188px; overflow: hidden;
    background: linear-gradient(90deg, #f4f4f4 0%, #ffffff 45%, #f2f2f2 100%);
  }
  .banner--insurance { top: 211px; }
  .banner--concept   { top: 405px; }
  .banner--beach     { top: 600px; }
  .banner--ski       { top: 795px; }

  .banner .facet { position: absolute; inset: 0; width: 100%; height: 100%; }

  .portrait {
    position: absolute; left: 10px; top: 14px; width: 160px; height: 174px;
    background: radial-gradient(ellipse at 50% 30%, #cfcfcf 0%, #9a9a9a 35%, #2e2e2e 70%, #1c1c1c 100%);
    clip-path: polygon(28% 0, 72% 0, 80% 40%, 100% 70%, 100% 100%, 0 100%, 0 70%, 20% 40%);
  }

  .brand { position: absolute; left: 12px; top: 10px; }
  .brand-name { display: block; font-weight: 500; font-size: 15px; color: var(--brand-red); letter-spacing: 0.2px; line-height: 1; }
  .brand-tag { display: block; font-size: 4.6px; color: var(--ink-soft); letter-spacing: 0.4px; margin-top: 3px; }

  .copy { position: absolute; right: 22px; text-align: right; }
  .headline { font-family: "Noto Serif", serif; font-weight: 400; line-height: 1; white-space: nowrap; }
  .sub { font-size: 7.2px; letter-spacing: 0.5px; text-transform: uppercase; white-space: nowrap; }

  .cta {
    position: absolute; left: 192px; top: 138px; width: 145px; height: 22px; border-radius: 11px;
    display: flex; align-items: center; justify-content: center;
    font-weight: 700; font-size: 12px; background: var(--brand-red); color: var(--paper);
  }
  .cta--light { background: var(--paper); color: var(--ink); }

  .banner--insurance .copy { top: 44px; }
  .banner--insurance .headline { color: var(--paper); font-size: 21px; line-height: 20px; }
  .banner--insurance .sub { color: var(--paper); margin-top: 9px; font-weight: 500; }
  .banner--insurance .sub u { text-underline-offset: 1px; }

  .banner--concept .copy { top: 46px; }
  .banner--concept .headline { color: var(--brand-red); font-size: 19px; line-height: 17px; }
  .banner--concept .points { list-style: none; margin-top: 10px; font-size: 5.3px; line-height: 9px; color: var(--ink-soft); letter-spacing: 0.3px; text-transform: uppercase; }

  .banner--beach .copy, .banner--ski .copy { top: 84px; }
  .banner--beach .headline { color: var(--paper); font-size: 18px; }
  .banner--beach .sub { color: var(--paper); margin-top: 8px; }
  .banner--ski .headline { color: var(--brand-red); font-size: 18px; }
  .banner--ski .sub { color: var(--ink-soft); margin-top: 8px; }

  .detail {
    position: absolute; width: 184px; height: 184px; border-radius: 50%; overflow: hidden;
    box-shadow: 0 4px 14px rgba(0,0,0,0.14);
  }
  .detail--suit  { left: 277px; top: 35px;  background: linear-gradient(160deg, #e6e6e6 0%, #9c9c9c 40%, #2a2a2a 75%); }
  .detail--suit::after { content: ""; position: absolute; right: 0; top: 20px; width: 45px; height: 120px; background: var(--brand-red-dark); clip-path: polygon(100% 0, 100% 100%, 0 100%); }
  .detail--desk  { left: 81px;  top: 371px; background: linear-gradient(120deg, #9a9a9a 0%, #dedede 30%, #f1f1f1 60%, #e4e4e4 100%); }
  .detail--desk .fragment { position: absolute; left: 95px; top: 142px; font-size: 13px; font-weight: 500; color: var(--ink-soft); letter-spacing: 0.6px; }
  .detail--desk .fragment-red { position: absolute; left: 166px; top: 70px; font-family: "Noto Serif", serif; font-size: 46px; color: var(--brand-red); line-height: 1; }
  .detail--beach { left: 615px; top: 640px; background: linear-gradient(175deg, #7d98a4 0%, #3aa9c7 25%, #62c6d4 50%, #f1d8d3 62%, #47b9c8 80%, #2fa3b2 100%); }
  .detail--beach .fragment { position: absolute; left: -62px; top: 128px; font-family: "Noto Serif", serif; font-size: 48px; color: var(--paper); white-space: nowrap; line-height: 1; }
  .detail--ski   { left: 503px; top: 977px; background: radial-gradient(circle at 50% 55%, #3e4f66 0%, #5a7fa8 25%, #b9cde0 55%, #edf2f7 80%); }
</style>
</head>
<body>
<main class="board">

  <div class="detail detail--suit" role="img" aria-label="Nahaufnahme: Berater in Anzug und Krawatte, schwarz-weiß, mit rotem Eckakzent"></div>

  <section class="banner banner--insurance">
    <svg class="facet" viewBox="0 0 359 188" aria-hidden="true">
      <defs>
        <linearGradient id="redField" x1="0" y1="0" x2="1" y2="1">
          <stop offset="0" stop-color="#e0303a"/><stop offset="1" stop-color="#c01a23"/>
        </linearGradient>
      </defs>
      <polygon points="150,0 230,0 180,70" fill="#e9e9e9"/>
      <polygon points="228,0 359,0 359,188 140,188" fill="url(#redField)"/>
      <polygon points="228,0 290,0 200,95" fill="#ffffff" opacity="0.08"/>
    </svg>
    <div class="portrait" role="img" aria-label="Porträtfoto des Beraters im Anzug, schwarz-weiß"></div>
    <div class="brand"><span class="brand-name">veltrama</span><span class="brand-tag">FINANCE CONSULTING</span></div>
    <div class="copy">
      <h2 class="headline">Richtige<br>Versicherung<br>Finden</h2>
      <p class="sub">Sparen Sie bis zu <u>€200</u> pro Jahr</p>
    </div>
    <span class="cta cta--light">www.veltrama.de</span>
  </section>

  <div class="detail detail--desk" role="img" aria-label="Nahaufnahme: Brillenträger neben Taschenrechnertasten">
    <span class="fragment">GANZHEIT</span><span class="fragment-red">F</span>
  </div>

  <section class="banner banner--concept">
    <svg class="facet" viewBox="0 0 359 188" aria-hidden="true">
      <defs>
        <linearGradient id="deskField" x1="0" y1="0" x2="1" y2="1">
          <stop offset="0" stop-color="#d6d6d6"/><stop offset="0.5" stop-color="#f0f0f0"/><stop offset="1" stop-color="#ffffff"/>
        </linearGradient>
      </defs>
      <polygon points="150,0 230,0 180,70" fill="#e9e9e9"/>
      <polygon points="228,0 359,0 359,60 190,70" fill="url(#deskField)" role="img" aria-label="Taschenrechner, Tabelle und Kugelschreiber"/>
    </svg>
    <div class="portrait" role="img" aria-label="Porträtfoto des Beraters im Anzug, schwarz-weiß"></div>
    <div class="brand"><span class="brand-name">veltrama</span><span class="brand-tag">FINANCE CONSULTING</span></div>
    <div class="copy">
      <h2 class="headline">Ihr<br>Finanzkonzept</h2>
      <ul class="points">
        <li>Ganzheitliche Betrachtung der Finanzsituation</li>
        <li>Nie mehr Kündigungstermine verpassen</li>
        <li>Richtige Versicherung finden</li>
        <li>Nur soviel bezahlen wie nötig</li>
      </ul>
    </div>
    <span class="cta">www.veltrama.de</span>
  </section>

  <section class="banner banner--beach">
    <svg class="facet" viewBox="0 0 359 188" aria-hidden="true">
      <defs>
        <linearGradient id="seaField" x1="0" y1="0" x2="0.4" y2="1">
          <stop offset="0" stop-color="#6f9fb0"/><stop offset="0.2" stop-color="#2c9fc2"/>
          <stop offset="0.35" stop-color="#f0d4d0"/><stop offset="0.5" stop-color="#4cc0cc"/>
          <stop offset="1" stop-color="#7fdde2"/>
        </linearGradient>
      </defs>
      <polygon points="150,0 230,0 180,70" fill="#e9e9e9"/>
      <polygon points="215,0 359,0 359,188 120,188" fill="url(#seaField)" role="img" aria-label="Tropischer Strand mit Palmwedel und türkisem Meer"/>
    </svg>
    <div class="portrait" role="img" aria-label="Porträtfoto des Beraters im Anzug, schwarz-weiß"></div>
    <div class="brand"><span class="brand-name">veltrama</span><span class="brand-tag">FINANCE CONSULTING</span></div>
    <div class="copy">
      <h2 class="headline">Familienurlaub?</h2>
      <p class="sub">Keine Überraschungen erleben</p>
    </div>
    <span class="cta">www.veltrama.de</span>
  </section>

  <div class="detail detail--beach" role="img" aria-label="Nahaufnahme: Sandbank und türkises Meer mit Palmwedel">
    <span class="fragment">Familienurlaub?</span>
  </div>

  <section class="banner banner--ski">
    <svg class="facet" viewBox="0 0 359 188" aria-hidden="true">
      <defs>
        <linearGradient id="snowField" x1="0" y1="0" x2="0" y2="1">
          <stop offset="0" stop-color="#4f86c4"/><stop offset="0.35" stop-color="#dfe8f1"/>
          <stop offset="0.7" stop-color="#ffffff"/><stop offset="1" stop-color="#ffffff"/>
        </linearGradient>
      </defs>
      <polygon points="150,0 230,0 180,70" fill="#e9e9e9"/>
      <polygon points="228,0 359,0 359,188 140,188" fill="url(#snowField)" role="img" aria-label="Skifahrer im Sessellift vor verschneiten Bergen"/>
    </svg>
    <div class="portrait" role="img" aria-label="Porträtfoto des Beraters im Anzug, schwarz-weiß"></div>
    <div class="brand"><span class="brand-name">veltrama</span><span class="brand-tag">FINANCE CONSULTING</span></div>
    <div class="copy">
      <h2 class="headline">Familienurlaub?</h2>
      <p class="sub">Keine Überraschungen erleben</p>
    </div>
    <span class="cta">www.veltrama.de</span>
  </section>

  <div class="detail detail--ski" role="img" aria-label="Nahaufnahme: Skifahrer in bunter Kleidung im Sessellift"></div>

</main>
</body>
</html>
```